Property Management Company Business Cards

Need business cards for a property management company located in Michigan. We manage houses for clients all over the world. Young and modern company, looking for eye catching design. Please work with the attached logo.

Industry/Entity Type

Property Management

Requirements
Must have
• Need lines for address, telephone number, fax number, web site.

Also lines for name, and job title

```html
<!DOCTYPE html>
<html lang="en">
<head>
<meta charset="utf-8">
<title>Lakeshore Harbor Management – Business Card</title>
<link rel="stylesheet" href="https://fonts.googleapis.com/css2?family=Source+Sans+3:wght@400;600;700&display=swap">
<style>
  :root {
    --backdrop: #e4e7ea;
    --card: #f5f6f7;
    --card-edge: #dde1e4;
    --ink: #3c3c3f;
    --ink-soft: #4a4a4d;
    --accent: #1ea4cc;
  }
  * { box-sizing: border-box; margin: 0; padding: 0; }
  html, body {
    width: 1200px; height: 900px; overflow: hidden;
    background: var(--backdrop);
    font-family: "Source Sans 3", "Myriad Pro", sans-serif;
  }
  .business-card {
    position: absolute; left: 75px; top: 150px;
    width: 1050px; height: 600px;
    background: var(--card);
    border: 1px solid var(--card-edge);
    border-radius: 26px;
    overflow: hidden;
    box-shadow: 0 10px 30px rgba(0,0,0,0.08);
  }
  .brand-symbol {
    position: absolute; left: 590px; top: 40px;
    width: 520px; height: 520px;
  }
  .brand {
    position: absolute; left: 34px; top: 62px;
    display: flex; align-items: center; gap: 14px;
  }
  .brand-dot {
    width: 34px; height: 34px; border-radius: 50%;
    background: var(--accent);
  }
  .brand-name {
    font-weight: 700; font-size: 29px; letter-spacing: 0.5px;
    color: var(--ink); text-transform: uppercase;
  }
  .person { position: absolute; left: 52px; top: 228px; }
  .person-name {
    font-weight: 600; font-size: 38px; color: var(--accent); line-height: 1.1;
  }
  .person-title {
    font-size: 26px; color: var(--ink-soft); margin-top: 4px;
  }
  .postal {
    position: absolute; left: 52px; top: 352px;
    font-size: 26px; line-height: 38px; color: var(--ink-soft);
  }
  .contact-list {
    position: absolute; left: 52px; top: 452px;
    list-style: none; font-size: 25px; line-height: 37px; color: var(--ink-soft);
  }
  .contact-list li { display: flex; align-items: center; gap: 12px; }
  .contact-icon { width: 22px; height: 22px; flex: none; }
</style>
</head>
<body>
  <article class="business-card">
    <svg class="brand-symbol" viewBox="0 0 520 520" role="img" aria-label="Large brand symbol decoration">
      <circle cx="260" cy="260" r="260" fill="var(--ink)"/>
    </svg>

    <header class="brand">
      <span class="brand-dot"></span>
      <span class="brand-name">Lakeshore Harbor Management</span>
    </header>

    <section class="person">
      <h1 class="person-name">Owen Carter</h1>
      <p class="person-title">Marketing Manager</p>
    </section>

    <address class="postal" style="font-style:normal">
      PO Box 518<br>
      Fairview SA 5092
    </address>

    <ul class="contact-list">
      <li>
        <svg class="contact-icon" viewBox="0 0 24 24" aria-hidden="true">
          <path fill="var(--accent)" d="M3 9c0-3 4-5 9-5s9 2 9 5v2h-5V9c-1-1-7-1-8 0v2H3zM6 12h12l2 7H4z"/>
        </svg>
        <span>(08) 8340 5512</span>
      </li>
      <li>
        <svg class="contact-icon" viewBox="0 0 24 24" aria-hidden="true">
          <rect x="6" y="3" width="12" height="6" fill="none" stroke="var(--accent)" stroke-width="2"/>
          <rect x="3" y="9" width="18" height="9" rx="1" fill="var(--accent)"/>
          <rect x="6" y="15" width="12" height="6" fill="var(--card)" stroke="var(--accent)" stroke-width="2"/>
        </svg>
        <span>0415 762 308</span>
      </li>
      <li>
        <svg class="contact-icon" viewBox="0 0 24 24" aria-hidden="true">
          <rect x="2.5" y="5.5" width="19" height="13" fill="none" stroke="var(--accent)" stroke-width="2"/>
          <path d="M3 6l9 7 9-7" fill="none" stroke="var(--accent)" stroke-width="2"/>
        </svg>
        <span>owen@lakeshoreharbor.com</span>
      </li>
      <li>
        <svg class="contact-icon" viewBox="0 0 24 24" aria-hidden="true">
          <circle cx="12" cy="12" r="10" fill="var(--accent)"/>
          <path d="M2 12h20M12 2c-4 4-4 16 0 20M12 2c4 4 4 16 0 20" fill="none" stroke="var(--card)" stroke-width="1.6"/>
        </svg>
        <span>www.lakeshoreharbor.com</span>
      </li>
    </ul>
  </article>
</body>
</html>
```